Business Card Design for Music Therapy Startup

I began my journey attending the Brantwell College School of Music to become a music educator before changing my degree and graduating with a Bachelor's degree in Music with an Outside Field in Psychology in 2008. From there, I attended Dunmore State University where I completed my Bachelor's Equivalency degree in Music Therapy. I became a Board Certified - Music Therapist almost 3 years ago and have since specialized in geriatrics, bereavement and end of life care. I anticipate completing my Master's Degree in Music Therapy in May, 2015, from Kessington State University.

In August of 2014 I completed advanced training in Neurologic Music Therapy (NMT) allowing me to also address speech and language, sensorimotor and cognitive deficits which develop as a result of neurologic injury and disease processes. Parkinson's Disease, Stroke, Traumatic Brain Injury and Dementia are amongst some of the neurologic conditions which may be treated with NMT.

My Philosophy: I strive to provide professional, genuine and compassionate care to all individuals, families and facilities that I serve. I use evidence-based and standardized music-based therapeutic techniques to achieve results which are documented, while complying with privacy regulations. I work with my patients and families to assess the primary goals to be addressed and to establish the most effective treatment plan to facilitate the best results.

Industry/Entity Type

Training

Contact Information for Business Card

Lorena J. Deskow, MT-BC
Neurologic Music Therapist

Riverbend Sound Therapy, LLC

555.204.6617

www.riverbendsoundtherapy.example
riverbendRST@mailbox.example

```html
<!DOCTYPE html>
<html lang="en">
<head>
<meta charset="utf-8">
<title>Lorena J. Deskow – Riverbend Sound Therapy business card</title>
<link href="https://fonts.googleapis.com/css2?family=Poppins:ital,wght@0,500;0,600;1,600&display=swap" rel="stylesheet">
<style>
  :root {
    --paper: #ffffff;
    --name-red: #e0453a;
    --name-red-light: #f27a5e;
    --name-shadow: rgba(120, 30, 20, 0.35);
    --title-green: #3c9a5c;
    --contact-orange: #f26a2e;
    --swirl-lime: #c8ea8a;
    --swirl-pink: #f06fd0;
    --swirl-cyan: #6fe0f0;
    --swirl-green: #2f7a3a;
    --brain-pink: #e58b86;
    --brain-cream: #efdcae;
    --ring-dark: #2a2a3a;
  }
  html, body {
    margin: 0;
    padding: 0;
    overflow: hidden;
    background: var(--paper);
  }
  .card {
    position: relative;
    width: 1200px;
    height: 702px;
    background: var(--paper);
    overflow: hidden;
    font-family: "Poppins", "Century Gothic", sans-serif;
  }
  .artwork {
    position: absolute;
    inset: 0;
  }
  .name {
    position: absolute;
    left: 50px;
    top: 96px;
    margin: 0;
    font-size: 52px;
    font-weight: 600;
    letter-spacing: 1px;
    line-height: 1;
    text-transform: uppercase;
    background: linear-gradient(180deg, var(--name-red-light), var(--name-red) 60%);
    -webkit-background-clip: text;
    background-clip: text;
    color: transparent;
    filter: drop-shadow(2px 3px 2px var(--name-shadow));
  }
  .credentials {
    position: absolute;
    left: 69px;
    top: 156px;
    margin: 0;
    color: var(--title-green);
    font-size: 24px;
    font-weight: 600;
    font-style: italic;
    line-height: 31px;
  }
  .credentials .practice {
    display: block;
    padding-left: 31px;
  }
  .contact {
    position: absolute;
    left: 58px;
    top: 466px;
    margin: 0;
    font-style: normal;
    color: var(--contact-orange);
    font-weight: 500;
  }
  .contact .phone { display: block; font-size: 23px; line-height: 27px; }
  .contact .web { display: block; font-size: 18px; line-height: 25px; font-weight: 600; }
  .contact .email { display: block; font-size: 25px; line-height: 30px; }
</style>
</head>
<body>
<main class="card">
  <svg class="artwork" width="1200" height="702" viewBox="0 0 1200 702" aria-hidden="false">
    <defs>
      <radialGradient id="swirl-field" cx="0.62" cy="0.45" r="0.6">
        <stop offset="0" stop-color="var(--swirl-pink)" stop-opacity="0.35"/>
        <stop offset="0.45" stop-color="var(--swirl-cyan)" stop-opacity="0.25"/>
        <stop offset="0.8" stop-color="var(--swirl-lime)" stop-opacity="0.35"/>
        <stop offset="1" stop-color="var(--swirl-lime)" stop-opacity="0"/>
      </radialGradient>
      <linearGradient id="swirl-stream" x1="0" y1="0" x2="1" y2="0">
        <stop offset="0" stop-color="var(--swirl-lime)" stop-opacity="0.35"/>
        <stop offset="0.5" stop-color="var(--swirl-pink)" stop-opacity="0.3"/>
        <stop offset="1" stop-color="var(--swirl-green)" stop-opacity="0.35"/>
      </linearGradient>
      <radialGradient id="brain-fill" cx="0.5" cy="0.45" r="0.55">
        <stop offset="0" stop-color="var(--brain-cream)"/>
        <stop offset="0.7" stop-color="var(--brain-pink)"/>
        <stop offset="1" stop-color="var(--brain-pink)" stop-opacity="0.85"/>
      </radialGradient>
    </defs>

    <path class="swirl-field" role="img" aria-label="Marbled multicolour swirl pattern surrounding the brain"
          d="M560 0 H1200 V702 H600 C620 640 560 600 600 540 C640 480 560 440 620 380 C660 330 600 260 650 200 C700 130 600 80 560 0 Z"
          fill="url(#swirl-field)"/>

    <path class="swirl-stream" role="img" aria-label="Flowing marbled swirl band across the card"
          d="M0 300 C80 230 170 230 240 265 C320 300 400 215 470 230 C540 245 580 210 640 240 L640 370 C560 360 520 390 440 365 C360 340 300 400 220 380 C140 360 80 410 0 400 Z"
          fill="url(#swirl-stream)"/>

    <circle class="brain-frame" cx="970" cy="290" r="166" fill="none" stroke="var(--ring-dark)" stroke-width="4"/>
    <circle class="brain-frame-inner" cx="970" cy="290" r="154" fill="var(--paper)"/>
    <ellipse class="brain-illustration" role="img" aria-label="Illustration of a human brain in sagittal cross-section"
             cx="965" cy="300" rx="128" ry="120" fill="url(#brain-fill)"/>
  </svg>

  <h1 class="name">Lorena J. Deskow</h1>
  <p class="credentials">
    <span class="role">MT-BC Neurologic Music Therapist</span>
    <span class="practice">Riverbend Sound Therapy, LLC</span>
  </p>
  <address class="contact">
    <span class="phone">555.204.6617</span>
    <span class="web">www.riverbendsoundtherapy.example</span>
    <span class="email">riverbendRST@mailbox.example</span>
  </address>
</main>
</body>
</html>
```